Creative Fitness Studio Feature Wall

Two feature walls within functional fitness studio, they need to be on brand and have a WOW factor.
Designed to inspire and motivate people to live a fit and healthy lifestyle whilst working out and bringing life to the studio, as an uplifting and inviting environment.

Please see current walls and also visit website www.velta4.com.au for inspiration.
Updates

Target Market(s)

health and fitness, healthy lifestyle

Industry/Entity Type

Fitness

Font styles to use
Other font styles liked:
• gothic

Colors

Designer to choose colors to be used in the design.

Requirements
Must have
• inspiration from website www.velta4.com.au ........... brand consistency
Nice to have
• WOW factor......... walk into the gym and it draws your attention.
Should not have
• Overly muscly people (bodybuilders)

```html
<!DOCTYPE html>
<html lang="en">
<head>
<meta charset="utf-8">
<title>Velta4 Fitness – Studio Feature Wall</title>
<link rel="stylesheet" href="https://fonts.googleapis.com/css2?family=PT+Serif:wght@700&display=swap">
<style>
  :root {
    --wall: #e7e6e3;
    --wall-pattern: #dcdbd8;
    --ink: #1b1b1b;
    --green: #7db843;
    --cream: #efe9dc;
    --figure: #bcbbb7;
  }
  html, body { margin: 0; padding: 0; overflow: hidden; background: #ffffff; }
  .feature-wall {
    position: relative;
    width: 1200px;
    height: 774px;
    overflow: hidden;
    font-family: "PT Serif", Georgia, serif;
    font-weight: 700;
    color: var(--ink);
  }
  .wall-pattern {
    position: absolute; inset: 0;
    background: linear-gradient(135deg, var(--wall) 0%, var(--wall-pattern) 100%);
  }
  .shapes { position: absolute; left: 0; top: 0; }
  .figure {
    position: absolute;
    background: var(--figure);
    border-radius: 10px;
  }
  .quote { position: absolute; margin: 0; line-height: 1.08; }
  .quote .lead { display: block; color: var(--green); }
  .quote-courage { left: 118px; top: 78px; color: var(--cream); font-size: 30px; }
  .quote-courage .lead { color: var(--cream); font-size: 50px; }
  .quote-dreams { left: 172px; top: 418px; color: var(--cream); font-size: 27px; }
  .quote-dreams .lead { color: var(--cream); font-size: 46px; }
  .quote-easier { left: 545px; top: 150px; font-size: 32px; }
  .quote-easier .lead { font-size: 44px; }
  .quote-best { left: 545px; top: 520px; font-size: 32px; }
  .quote-best .lead { font-size: 50px; }
  .quote-clear { left: 860px; top: 150px; font-size: 36px; }
  .quote-clear .lead { font-size: 58px; }
  .quote-fear { left: 860px; top: 385px; font-size: 36px; }
  .quote-fear .lead { font-size: 58px; }
  .brand-name {
    position: absolute; right: 40px; bottom: 60px; margin: 0;
    font-size: 50px; color: var(--ink);
  }
</style>
</head>
<body>
<main class="feature-wall">
  <div class="wall-pattern" role="img" aria-label="Faint repeating pattern of fitness equipment across the wall"></div>

  <svg class="shapes" width="1200" height="774" viewBox="0 0 1200 774" aria-hidden="true">
    <polygon class="shape-black" points="30,40 470,40 250,430" fill="#1b1b1b"/>
    <polygon class="shape-green" points="250,320 480,560 250,774 20,560" fill="#7db843"/>
  </svg>

  <div class="figure" role="img" aria-label="Silhouette of a woman in a push-up pose" style="left:380px;top:18px;width:120px;height:60px;"></div>
  <div class="figure" role="img" aria-label="Barbell icon" style="left:210px;top:300px;width:80px;height:40px;"></div>
  <div class="figure" role="img" aria-label="Silhouette of a man flipping a tyre" style="left:620px;top:20px;width:170px;height:160px;"></div>
  <div class="figure" role="img" aria-label="Silhouette of a person lifting dumbbells" style="left:620px;top:450px;width:95px;height:120px;"></div>
  <div class="figure" role="img" aria-label="Kettlebell icon" style="left:935px;top:30px;width:100px;height:110px;"></div>
  <div class="figure" role="img" aria-label="Silhouette of a cyclist on an exercise bike" style="left:1060px;top:320px;width:125px;height:190px;"></div>

  <p class="quote quote-courage"><span class="lead">Courage</span>Is What Keeps<br>You Going</p>
  <p class="quote quote-dreams"><span class="lead">The</span>Difference<br>Between<br>Dreams and<br>Reality is<br>Action</p>
  <p class="quote quote-easier"><span class="lead">IT</span>Never Gets<br>Easier You<br>Just Get<br>Better</p>
  <p class="quote quote-best"><span class="lead">Be</span>the Best<br>Version of You</p>
  <p class="quote quote-clear"><span class="lead">Clear</span>Your Mind<br>Of Can’t</p>
  <p class="quote quote-fear"><span class="lead">Fear</span>Is What<br>Stops You</p>

  <p class="brand-name">Velta4 Fitness</p>
</main>
</body>
</html>
```